Brisel Home Care Brochure for Recruiting Clients

I need a brochure made for a home care company called 'Brisel Home Care'. I have uploaded the logo, location, and a few items about our company and what it offers. The final design should communicate trust and respect for patients and their families. I will probably be changing the phone number in the next few days so will need to add a new number and more serving locations.

Industry/Entity Type

Home Health Care

Colors
0555a3
ffffff
3176b5
85acd3
0392cd

Requirements
Must have
• Hello All,
• Thank you kindly for your patience. Please add the changes below to the brochures:
• Phone number: 571-555-0143
• Email: briselhc@quorvamail.com
• Homepage: [Non image link removed]Service Locations: Ashford County, Belmont County, Carver County, Linden County, Westbrook County
• Also please note the additional sentence at the end of the following key points:
• ABOUT US:
• Brisel serves to give patients the personal care they need in order for them to continue to live dignified and independent lives in the comfort of their homes. We begin by assessing and understanding our patient’s individual needs and met those needs through selectively assigning qualified, trustworthy and compassionate home care aids. Brisel holds great pride in keeping our client’s health, quality of life and well-being central in the design and delivery of our services. Our services can prevent re-hospitalization, postpone institutionalization, and reduce the need for urgent care.
• ABOUT OUR SERVICE PROVIDERS:
• We go through a rigorous in-depth application process with all of our service providers, so that you can rest assure that your home care provider is most qualified to meet your needs. Our application process also includes a thorough screening, criminal background check, DMV driving history and a comprehensive exam. Our service providers are trained, monitored, and tested continuously to meet our high standards of work ethic and professionalism. Our care providers are covered by professional liability, bonding, and workers’ compensation insurance. At Brisel teamwork among members is of key importance and it is how we conduct our day to day business. We work as a team with family, patient and their provider in developing an ideal care plan for the patient.
• OUR SERVICES:
• Companionship Services Include:
• - Offer companionship and conversation - Supervise home maintenance
• - Mail bills and letters
• - Provide reminders for appointments
• - Arrange appointments
• - Maintain calendar
• - Plan visits, outings and trips
• - Visit friends
• - Prepare grocery list
• - Assist with clothing selection
• - Stimulate mental awareness
• - Aid with reading
• - Monitor diet and eating
• - Check food expirations
• - Assist with morning and wake-up
• - Assist with evening and tuck-in
• - Provide respite care
• - Provide medication reminders
• - Assist with walking
• - Write letters and correspondence
• - Organize mail
• - Care for house plants
• - Answer the door
• - Assist with entertaining
• - Play games and cards
• - Rent and play movies
• - Oversee home deliveries
• - Supervise home maintenance
• - Discuss current and historical events - Reminisce about the past
• Home Helper Services Include:
• - Assist with laundry and ironing
• - Organize and clean closets
• - Assist with pet care
• - Attend social and sporting events - Accompany to lunch or dinner
• - Care for Alzhiemers
• - Change linens
• - Dust furniture
• - Drop off and pick up dry cleaning
• - Escort for shopping and errands
• - Escort to appointments
• - Escort to religious services
• - Help with airport task
• - Pick up prescriptions
• - Make beds
• - Prepare meals
• - Plan, prepare, and clean-up meals - Prepare future meals
• - Provide light housekeeping
• - Take out garbage
• Personal Services Include:
• - Ambulation
• - Bathing
• - Cognitive impairment - Mobility
• - Transferring
• - Incontinence
• - Dressing
• - Eating
• - Grooming
Nice to have
• Nice pictures of elderly clients with helpers or nurse.

```html
<!DOCTYPE html>
<html lang="en">
<head>
<meta charset="utf-8">
<title>Brisel Home Care Brochure</title>
<link href="https://fonts.googleapis.com/css2?family=Open+Sans:wght@400;600;700;800&display=swap" rel="stylesheet">
<style>
:root{
  --navy:#0555a3;
  --blue:#3176b5;
  --sky:#85acd3;
  --cyan:#0392cd;
  --white:#ffffff;
  --ink:#4a4f57;
  --page:#eceef1;
}
*{margin:0;padding:0;box-sizing:border-box}
html,body{width:779px;height:1200px;overflow:hidden;background:var(--page);font-family:"Open Sans",Arial,sans-serif;color:var(--ink)}
.sheet{position:absolute;left:45px;width:690px;background:var(--white);box-shadow:0 2px 8px rgba(0,0,0,.18);overflow:hidden}
.sheet--outside{top:45px;height:585px}
.sheet--inside{top:650px;height:510px}
.panel{position:absolute;top:0;width:230px;height:100%;overflow:hidden}
.panel--1{left:0}.panel--2{left:230px}.panel--3{left:460px}
.photo{position:absolute;left:0;width:100%}
.wave{position:absolute;left:0;width:100%}
h2{font-size:11px;font-weight:800;color:var(--navy);letter-spacing:.3px;text-transform:uppercase}
p{font-size:7.6px;line-height:10.6px;margin-top:7px;text-align:justify}

/* outside */
.about{position:absolute;left:14px;top:16px;width:202px}
.contact-top{position:absolute;top:0;left:0;width:100%;height:175px;background:linear-gradient(180deg,#6f95be,#3f6fa6);padding:22px 14px 0;text-align:center;color:var(--white)}
.contact-top h2{color:var(--white);font-size:12px}
.contact-top .address{font-size:8px;line-height:11px;margin-top:12px;font-weight:600}
.contact-top .areas{font-size:7.4px;line-height:10px;margin-top:10px}
.map{position:absolute;left:70px;top:186px;width:90px;height:90px;border-radius:50%;background:radial-gradient(circle,#f3f4f2,#dfe3e6);border:3px solid var(--white);box-shadow:0 1px 4px rgba(0,0,0,.25)}
.callout{position:absolute;left:0;top:405px;width:100%;text-align:center;color:var(--white)}
.callout .phone{font-size:9.5px;font-weight:700}
.callout .email{font-size:8.5px;font-weight:600;margin-top:3px}
.web-band{position:absolute;left:0;bottom:24px;width:100%;height:24px;background:var(--white);text-align:center;font-size:9px;font-weight:700;color:var(--navy);line-height:24px}
.brand{position:absolute;left:0;top:420px;width:100%;text-align:center}
.brand-mark{display:block;width:34px;height:34px;margin:0 auto 8px;background:var(--navy)}
.brand-name{font-size:17px;font-weight:700;color:var(--navy)}

/* inside */
.providers{position:absolute;left:14px;top:222px;width:202px}
.providers h2{font-size:9.5px}
.companion{background:linear-gradient(180deg,var(--navy),var(--blue));color:var(--white);padding:14px 12px}
.companion h2{color:var(--white);font-size:8.6px}
.ticks{list-style:none;margin-top:8px}
.ticks li{position:relative;font-size:8px;line-height:14.5px;padding-left:15px}
.ticks li::before{content:"";position:absolute;left:2px;top:4px;width:4px;height:7px;border:solid var(--white);border-width:0 2px 2px 0;transform:rotate(45deg)}
.helper{padding:13px 12px}
.helper h2{font-size:8.4px}
.helper h2.next{margin-top:10px}
.bullets{list-style:none;margin-top:4px}
.bullets li{position:relative;font-size:7.6px;line-height:11.8px;padding-left:9px}
.bullets li::before{content:"";position:absolute;left:1px;top:4.5px;width:3px;height:3px;background:var(--cyan)}
</style>
</head>
<body>

<section class="sheet sheet--outside">
  <div class="panel panel--1">
    <div class="about">
      <h2>About Us</h2>
      <p>Brisel serves to give patients the personal care they need in order for them to continue to live dignified and independent lives in the comfort of their homes.</p>
      <p>We begin by assessing and understanding our patient’s individual needs and met those needs through selectively assigning qualified, trustworthy and compassionate home care aids.</p>
      <p>Brisel holds great pride in keeping our client’s health, quality of life and well-being central in the design and delivery of our services. Our services can prevent re-hospitalization, postpone institutionalization, and reduce the need for urgent care.</p>
    </div>
    <div class="photo" role="img" aria-label="Photo of a smiling elderly couple at home" style="top:285px;height:300px;background:linear-gradient(160deg,#d8c6b4,#a99480)"></div>
    <svg class="wave" style="top:255px" width="230" height="70" viewBox="0 0 230 70" preserveAspectRatio="none">
      <path d="M0 0H230V18C160 55 80 20 0 48Z" fill="var(--white)"/>
      <path d="M0 48C80 20 160 55 230 18V30C160 66 80 34 0 60Z" fill="var(--navy)"/>
      <path d="M0 60C80 34 160 66 230 30V36C160 72 80 42 0 66Z" fill="var(--sky)"/>
    </svg>
  </div>

  <div class="panel panel--2">
    <div class="contact-top" role="img" aria-label="Faded photo of a caregiver with a client, tinted blue">
      <h2>Contact Us</h2>
      <div class="address">612 Harlow Street,<br>Maple Ridge, VA 20519</div>
      <div class="areas">Service Locations: Ashford County, Belmont County, Carver County, Linden County, Westbrook County</div>
    </div>
    <div class="map" role="img" aria-label="Location map"></div>
    <svg class="wave" style="top:300px" width="230" height="285" viewBox="0 0 230 285" preserveAspectRatio="none">
      <path d="M0 40C70 70 150 10 230 30V285H0Z" fill="var(--sky)"/>
      <path d="M0 52C70 82 150 22 230 42V285H0Z" fill="var(--navy)"/>
    </svg>
    <div class="callout">
      <div class="phone">Call us now at 571-555-0143</div>
      <div class="email">briselhc@quorvamail.com</div>
    </div>
    <div class="web-band">www.briselhomecare.org</div>
  </div>

  <div class="panel panel--3">
    <div class="photo" role="img" aria-label="Photo of a nurse caring for an elderly woman" style="top:0;height:340px;background:linear-gradient(150deg,#e8ecef,#a8b8c8 55%,#c9b8a6)"></div>
    <svg class="wave" style="top:290px" width="230" height="80" viewBox="0 0 230 80" preserveAspectRatio="none">
      <path d="M0 30C80 70 160 10 230 40V80H0Z" fill="var(--white)"/>
      <path d="M0 20C80 60 160 0 230 30V40C160 10 80 70 0 30Z" fill="var(--navy)"/>
    </svg>
    <div class="brand">
      <span class="brand-mark"></span>
      <span class="brand-name">Brisel Home Care</span>
    </div>
  </div>
</section>

<section class="sheet sheet--inside">
  <div class="panel panel--1">
    <div class="photo" role="img" aria-label="Photo of a caregiver embracing an elderly man" style="top:0;height:215px;background:linear-gradient(150deg,#b7c6d6,#8ea3b8 50%,#c8b29c)"></div>
    <svg class="wave" style="top:170px" width="230" height="50" viewBox="0 0 230 50" preserveAspectRatio="none">
      <path d="M0 30C80 0 160 40 230 14V50H0Z" fill="var(--white)"/>
      <path d="M0 22C80 -8 160 32 230 6V14C160 40 80 0 0 30Z" fill="var(--navy)"/>
    </svg>
    <div class="providers">
      <h2>About Our Service Providers:</h2>
      <p>We go through a rigorous in-depth application process with all of our service providers, so that you can rest assure that your home care provider is most qualified to meet your needs.</p>
      <p>Our application process also includes a thorough screening, criminal background check, DMV driving history and a comprehensive exam. Our service providers are trained, monitored, and tested continuously to meet our high standards of work ethic and professionalism.</p>
      <p>Our care providers are covered by professional liability, bonding, and workers’ compensation insurance. At Brisel teamwork among members is of key importance and it is how we conduct our day to day business.</p>
      <p>We work as a team with family, patient and their provider in developing an ideal care plan for the patient.</p>
    </div>
  </div>

  <div class="panel panel--2 companion">
    <h2>Companionship Services Include:</h2>
    <ul class="ticks">
      <li>Offer companionship and conversation</li><li>Supervise home maintenance</li><li>Mail bills and letters</li><li>Provide reminders for appointments</li><li>Arrange appointments</li><li>Maintain calendar</li><li>Plan visits, outings and trips</li><li>Visit friends</li><li>Prepare grocery list</li><li>Assist with clothing selection</li><li>Stimulate mental awareness</li><li>Aid with reading</li><li>Monitor diet and eating</li><li>Check food expirations</li><li>Assist with morning and wake-up</li><li>Assist with evening and tuck-in</li><li>Provide respite care</li><li>Provide medication reminders</li><li>Assist with walking</li><li>Write letters and correspondence</li><li>Organize mail</li><li>Care for house plants</li><li>Answer the door</li><li>Assist with entertaining</li><li>Play games and cards</li><li>Rent and play movies</li><li>Oversee home deliveries</li><li>Supervise home maintenance</li><li>Discuss current and historical events</li><li>Reminisce about the past</li>
    </ul>
  </div>

  <div class="panel panel--3">
    <div class="helper">
      <h2>Home Helper Services Include:</h2>
      <ul class="bullets">
        <li>Assist with laundry and ironing</li><li>Organize and clean closets</li><li>Assist with pet care</li><li>Attend social and sporting events</li><li>Accompany to lunch or dinner</li><li>Care for Alzheimers</li><li>Change linens</li><li>Dust furniture</li><li>Drop off and pick up dry cleaning</li><li>Escort for shopping and errands</li><li>Escort to appointments</li><li>Escort to religious services</li><li>Help with airport task</li><li>Pick up prescriptions</li><li>Make beds</li><li>Prepare meals</li><li>Plan, prepare, and clean-up meals</li><li>Prepare future meals</li><li>Provide light housekeeping</li><li>Take out garbage</li>
      </ul>
      <h2 class="next">Personal Services Include:</h2>
      <ul class="bullets">
        <li>Ambulation</li><li>Bathing</li><li>Cognitive impairment</li><li>Mobility</li><li>Transferring</li><li>Incontinence</li><li>Dressing</li><li>Eating</li><li>Grooming</li>
      </ul>
    </div>
    <div class="photo" role="img" aria-label="Photo of a family of three generations smiling together" style="top:432px;height:78px;background:linear-gradient(150deg,#d9c3ad,#b09a86)"></div>
    <svg class="wave" style="top:420px" width="230" height="30" viewBox="0 0 230 30" preserveAspectRatio="none">
      <path d="M0 0H230V8C160 30 80 4 0 20Z" fill="var(--white)"/>
      <path d="M0 20C80 4 160 30 230 8V14C160 36 80 10 0 26Z" fill="var(--navy)"/>
    </svg>
  </div>
</section>

</body>
</html>
```